Gym Menu

Hi,

I would like to create a menu for my fitness center/ Dance school.

I do have a picture of how i would like it to look like ill attach it down there and instead of the Mexican looking icons i would like to have gym related icons example (Bar bell, dumbbells, etc..)

The menu will consist of the following

Smoothies
- Lagoon Waltz (20 SR)
(Kiwi, Pineapple, Banana, Grapes)
-Coral Drift (20 SR)
(Orange, Peach, Pineapple)
-Tidy Kick (20 SR)
(Carrot, Mango, Orange)
-Purple Thunder (20 SR)
(Blackberry, Raspberry, Banana)
-Cool Breeze (20 SR)
( Lemonade, Mint)
-Ruby Lantern (20 SR)
(Lemonade, Strawberry, Mint)

Mean Green Juices

-Quick Sprout (20SR)
(Cucumber, Celery, Green Apple, Spinach, Lemon, Ginger)
-Hop To It Now! (20 SR)
(Carrots, Apple, Beetroot)

Shake It Up

-Dusky Swirl (20 SR)
(Mocha, Skimmed Milk)

- Velvet Tumbler
(Chocolate, Skimmed Milk)

-Big Lift Zest

(Peanut Butter, Honey, Skimmed Milk, Banana) (20 SR)

Yummy Bites

- Zataar Croissant (10 SR)
- Cheese Croissant (10 SR)
- Plane Croissant (10 SR)
- Blueberry Muffin (7 SR)
- Chocolate Muffin (7 SR)
- Vanilla Muffin (7SR)
- Cookies (7 SR)
- Brownie (10 SR)
-Fresh Berry Popsicle (10 SR)
- Fresh Orange Popsicle (10 SR)

Make it Lite

-Garden Salad (15 SR)
-Greek Salad (15 SR)
-Ceaser Salad (15 SR)
-Italian Salad (15 SR)
- Tuna Sandwich (25 SR)
- Turkey Sandwich (25 SR)
- Chicken Sandwich (25 SR)
-Happy Patch Bowls (8SR)
- Mixed Nuts (10 SR)

Coffee and tea
- Americano (10 SR)
- Espresso (10 SR)
- Turkish Coffee (10 SR)
- Cappuccino (15 SR)
- Cafe Latte (15 SR)
-Hot Cacao (15 SR)
-Extra shor + 5SR

- Green Tea (10 SR)
- Earl Grey (10 SR)
- English Breakfast (10SR)

• The gyms color is orange ... i want this to be in the menu

the gyms name is vartomel i also want this in big somewhere

Colors of the menu should be

Orange
Yellow
green
red

all shades

```html
<!DOCTYPE html>
<html lang="en">
<head>
<meta charset="utf-8">
<title>Vartomel Menu</title>
<link href="https://fonts.googleapis.com/css2?family=Exo+2:wght@300;400&family=Quicksand:wght@400&family=Roboto+Slab:wght@700&display=swap" rel="stylesheet">
<style>
  :root {
    --paper: #f4e3cf;
    --paper-edge: #ead2b6;
    --brand: #e8552a;
    --heading: #1f4e57;
    --dots: #2a5a62;
    --smoothie: #2f8fd8;
    --juice: #25b394;
    --shake: #d9962a;
    --bite: #ea8a1e;
    --lite: #23a687;
    --coffee: #2f86c6;
    --desc: #6b6660;
    --price: #85807a;
    --icon: #cfae86;
  }
  * { margin: 0; padding: 0; box-sizing: border-box; }
  html, body { width: 1200px; height: 843px; overflow: hidden; }
  body {
    position: relative;
    background: radial-gradient(ellipse at 30% 35%, #f8ecdc 0%, var(--paper) 55%, var(--paper-edge) 100%);
    font-family: "Exo 2", sans-serif;
  }
  .page-fold { position: absolute; left: 599px; top: 0; width: 2px; height: 843px; background: rgba(180,150,120,.25); }
  .abs { position: absolute; }
  .icon { position: absolute; background: var(--icon); border-radius: 6px; opacity: .85; }

  .brand-name {
    position: absolute; left: 44px; width: 520px; top: 28px; text-align: center;
    font-family: "Roboto Slab", serif; font-weight: 700; font-size: 78px;
    color: var(--brand); letter-spacing: 2px; line-height: 1;
  }
  .brand-tag {
    position: absolute; left: 44px; width: 520px; top: 141px; text-align: center;
    font-family: "Quicksand", sans-serif; font-size: 19px; letter-spacing: 4.5px; color: #5d5a55;
  }

  .box { position: absolute; border: 2px dotted var(--dots); }
  .section-title {
    position: absolute; font-family: "Quicksand", sans-serif; font-weight: 400;
    color: var(--heading); line-height: 1; letter-spacing: 2px;
  }
  .section-title.big { font-size: 52px; }
  .section-title.mid { font-size: 37px; line-height: 1.08; }

  .feature { position: absolute; text-align: center; width: 230px; line-height: 1.25; }
  .feature.left { text-align: left; width: 240px; }
  .feature .name { font-size: 17.5px; }
  .feature .cost { font-size: 14px; color: var(--price); font-weight: 300; }
  .feature .desc { font-size: 14px; color: var(--desc); font-weight: 300; }
  .smoothie .name { color: var(--smoothie); }
  .juice .name { color: var(--juice); }
  .shake .name { color: var(--shake); }

  .item { position: absolute; font-size: 17px; line-height: 1; }
  .price { position: absolute; font-size: 14px; color: var(--price); font-weight: 300; text-align: right; width: 60px; line-height: 1; }
  .bite { color: var(--bite); }
  .lite { color: var(--lite); }
  .coffee { color: var(--coffee); }
</style>
</head>
<body>
<div class="page-fold"></div>

<!-- Masthead -->
<div class="icon" style="left:56px;top:118px;width:520px;height:12px;" role="img" aria-label="Barbell illustration behind the gym name"></div>
<div class="brand-name">VARTOMEL</div>
<div class="brand-tag">FITNESS CENTER / DANCE SCHOOL</div>

<!-- Drinks panel -->
<div class="box" style="left:44px;top:182px;width:511px;height:619px;"></div>
<div class="abs" style="left:44px;top:460px;width:511px;border-top:2px dotted var(--dots);"></div>
<div class="abs" style="left:298px;top:460px;height:341px;border-left:2px dotted var(--dots);"></div>

<div class="icon" style="left:72px;top:204px;width:62px;height:38px;border-radius:20px 20px 6px 6px;" role="img" aria-label="Kettlebell icon"></div>
<div class="section-title big" style="left:150px;top:200px;width:305px;text-align:center;">SMOOTHIES</div>
<div class="icon" style="left:469px;top:204px;width:62px;height:38px;border-radius:20px 20px 6px 6px;" role="img" aria-label="Kettlebell icon"></div>

<div class="feature smoothie" style="left:71px;top:268px;"><span class="name">Lagoon Waltz</span> <span class="cost">/ 20 SR</span><div class="desc">Kiwi, Pineapple, Banana, Grapes</div></div>
<div class="feature smoothie" style="left:71px;top:331px;"><span class="name">Coral Drift</span> <span class="cost">/ 20 SR</span><div class="desc">Orange, Peach, Pineapple</div></div>
<div class="feature smoothie" style="left:71px;top:393px;"><span class="name">Tidy Kick</span> <span class="cost">/ 20 SR</span><div class="desc">Carrot, Mango, Orange</div></div>
<div class="feature smoothie" style="left:296px;top:268px;"><span class="name">Purple Thunder</span> <span class="cost">/ 20 SR</span><div class="desc">Blackberry, Raspberry, Banana</div></div>
<div class="feature smoothie" style="left:296px;top:331px;"><span class="name">Cool Breeze</span> <span class="cost">/ 20 SR</span><div class="desc">Lemonade, Mint</div></div>
<div class="feature smoothie" style="left:296px;top:393px;"><span class="name">Ruby Lantern</span> <span class="cost">/ 20 SR</span><div class="desc">Lemonade, Strawberry, Mint</div></div>

<div class="section-title mid" style="left:44px;top:482px;width:254px;text-align:center;">MEAN GREEN<br>JUICES</div>
<div class="feature juice" style="left:55px;top:574px;width:230px;"><span class="name">Quick Sprout</span> <span class="cost">/ 20 SR</span><div class="desc">Cucumber, Celery, Green Apple,<br>Spinach, Lemon, Ginger</div></div>
<div class="feature juice" style="left:55px;top:646px;width:230px;"><span class="name">Hop To It Now!</span> <span class="cost">/ 20 SR</span><div class="desc">Carrots, Apple, Beetroot</div></div>
<div class="icon" style="left:88px;top:712px;width:166px;height:64px;opacity:.6;" role="img" aria-label="Dumbbell illustration"></div>

<div class="section-title mid" style="left:326px;top:486px;">SHAKE<br>IT UP</div>
<div class="icon" style="left:472px;top:488px;width:56px;height:88px;opacity:.6;" role="img" aria-label="Jump rope illustration"></div>
<div class="feature left shake" style="left:323px;top:592px;"><span class="name">Dusky Swirl</span> <span class="cost">/ 20 SR</span><div class="desc">Mocha, Skimmed Milk</div></div>
<div class="feature left shake" style="left:323px;top:646px;"><span class="name">Velvet Tumbler</span><div class="desc">Chocolate, Skimmed Milk</div></div>
<div class="feature left shake" style="left:323px;top:700px;"><span class="name">Big Lift Zest</span> <span class="cost">/ 20 SR</span><div class="desc">Peanut Butter, Honey,<br>Skimmed Milk, Banana</div></div>

<!-- Food & hot drinks panel -->
<div class="box" style="left:657px;top:36px;width:513px;height:766px;"></div>
<div class="abs" style="left:657px;top:284px;width:513px;border-top:2px dotted var(--dots);"></div>
<div class="abs" style="left:657px;top:552px;width:513px;border-top:2px dotted var(--dots);"></div>

<div class="section-title big" style="left:657px;top:58px;width:513px;text-align:center;">YUMMY BITES</div>
<div class="icon" style="left:1032px;top:112px;width:50px;height:76px;opacity:.6;" role="img" aria-label="Hand grip illustration"></div>
<div class="item bite" style="left:678px;top:131px;">Zataar Croissant</div><div class="price" style="left:814px;top:133px;">10 SR</div>
<div class="item bite" style="left:678px;top:161px;">Cheese Croissant</div><div class="price" style="left:814px;top:163px;">10 SR</div>
<div class="item bite" style="left:678px;top:190px;">Plane Croissant</div><div class="price" style="left:814px;top:192px;">10 SR</div>
<div class="item bite" style="left:678px;top:220px;">Blueberry Muffin</div><div class="price" style="left:814px;top:222px;">7 SR</div>
<div class="item bite" style="left:678px;top:250px;">Chocolate Muffin</div><div class="price" style="left:814px;top:252px;">7 SR</div>
<div class="item bite" style="left:904px;top:131px;">Vanilla Muffin</div><div class="price" style="left:1073px;top:133px;">7 SR</div>
<div class="item bite" style="left:904px;top:161px;">Cookies</div><div class="price" style="left:1073px;top:163px;">7 SR</div>
<div class="item bite" style="left:904px;top:190px;">Brownie</div><div class="price" style="left:1073px;top:192px;">10 SR</div>
<div class="item bite" style="left:904px;top:220px;">Fresh Berry Popsicle</div><div class="price" style="left:1073px;top:222px;">10 SR</div>
<div class="item bite" style="left:904px;top:250px;">Fresh Orange Popsicle</div><div class="price" style="left:1073px;top:252px;">10 SR</div>

<div class="section-title big" style="left:657px;top:304px;width:513px;text-align:center;">MAKE IT LITE</div>
<div class="item lite" style="left:678px;top:378px;">Garden Salad</div><div class="price" style="left:814px;top:380px;">15 SR</div>
<div class="item lite" style="left:678px;top:408px;">Greek Salad</div><div class="price" style="left:814px;top:410px;">15 SR</div>
<div class="item lite" style="left:678px;top:438px;">Ceaser Salad</div><div class="price" style="left:814px;top:440px;">15 SR</div>
<div class="item lite" style="left:678px;top:467px;">Italian Salad</div><div class="price" style="left:814px;top:469px;">15 SR</div>
<div class="item lite" style="left:678px;top:497px;">Tuna Sandwich</div><div class="price" style="left:814px;top:499px;">25 SR</div>
<div class="item lite" style="left:904px;top:378px;">Turkey Sandwich</div><div class="price" style="left:1073px;top:380px;">25 SR</div>
<div class="item lite" style="left:904px;top:408px;">Chicken Sandwich</div><div class="price" style="left:1073px;top:410px;">25 SR</div>
<div class="item lite" style="left:904px;top:438px;">Happy Patch Bowls</div><div class="price" style="left:1073px;top:440px;">8 SR</div>
<div class="item lite" style="left:904px;top:467px;">Mixed Nuts</div><div class="price" style="left:1073px;top:469px;">10 SR</div>
<div class="icon" style="left:912px;top:502px;width:92px;height:24px;border-radius:12px;opacity:.7;" role="img" aria-label="Dumbbell icon"></div>
<div class="icon" style="left:1036px;top:502px;width:92px;height:24px;border-radius:12px;opacity:.7;" role="img" aria-label="Dumbbell icon"></div>

<div class="section-title big" style="left:674px;top:576px;line-height:.82;">COFFEE<br>&amp; TEA</div>
<div class="icon" style="left:884px;top:588px;width:60px;height:180px;border-radius:30px;opacity:.6;" role="img" aria-label="Weight plate on a bar illustration"></div>
<div class="item coffee" style="left:678px;top:698px;">Green Tea</div><div class="price" style="left:814px;top:700px;">10 SR</div>
<div class="item coffee" style="left:678px;top:728px;">Earl Grey</div><div class="price" style="left:814px;top:730px;">10 SR</div>
<div class="item coffee" style="left:678px;top:758px;">English Breakfast</div><div class="price" style="left:814px;top:760px;">10 SR</div>
<div class="item coffee" style="left:960px;top:581px;">Americano</div><div class="price" style="left:1073px;top:583px;">10 SR</div>
<div class="item coffee" style="left:960px;top:610px;">Espresso</div><div class="price" style="left:1073px;top:612px;">10 SR</div>
<div class="item coffee" style="left:960px;top:640px;">Turkish Coffee</div><div class="price" style="left:1073px;top:642px;">10 SR</div>
<div class="item coffee" style="left:960px;top:669px;">Cappuccino</div><div class="price" style="left:1073px;top:671px;">15 SR</div>
<div class="item coffee" style="left:960px;top:698px;">Cafe Latte</div><div class="price" style="left:1073px;top:700px;">15 SR</div>
<div class="item coffee" style="left:960px;top:728px;">Hot Cacao</div><div class="price" style="left:1073px;top:730px;">15 SR</div>
<div class="item coffee" style="left:960px;top:758px;">Extra short</div><div class="price" style="left:1073px;top:760px;">+5 SR</div>
</body>
</html>
```